Business Card for premium dental clinic

We are a premium dental clinic based in Brasov, Romania with more than 15 year on the market, providing quality dental treatment made by a team of more specialized dentists, working with modern equipment as a solution to beautiful and healthy teeth.

Our current logo for the clinic use 2 square with colors black and gold - dr Corbescu - studio, using family fonts Bodoni, Myriad Pro and Segoe Print.
Depending on the printing we used some gold CMYK background or gold foil picture background or a gold gradient.
We want a business card:
- eye catching business card
- distinguished business card
- premium design
- to keep the color scheme of black and gold
- to attract the customers to spent time reading the information
- modern concept

```html
<!DOCTYPE html>
<html lang="en">
<head>
<meta charset="utf-8">
<title>dr Corbescu – Business Card</title>
<link rel="stylesheet" href="https://fonts.googleapis.com/css2?family=Montserrat:wght@500;700&family=Tinos:wght@700&family=Kaushan+Script&display=swap">
<style>
  :root {
    --gold: #f9dc14;
    --gold-deep: #f2cf0a;
    --black: #0b0b0b;
    --white: #ffffff;
  }
  * { margin: 0; padding: 0; box-sizing: border-box; }
  html, body { width: 1200px; height: 686px; overflow: hidden; background: var(--white); }
  .card {
    position: relative;
    width: 1200px;
    height: 686px;
    background: var(--white);
    overflow: hidden;
    font-family: "Tinos", "Times New Roman", serif;
  }
  .honeycomb-area {
    position: absolute;
    left: 530px;
    top: 0;
    width: 670px;
    height: 597px;
    background: linear-gradient(160deg, var(--gold) 0%, var(--gold-deep) 100%);
  }
  .banner {
    position: absolute;
    left: 0;
    top: 77px;
    width: 545px;
    height: 290px;
  }
  .banner-title {
    position: absolute;
    left: 21px;
    top: 96px;
    font-family: "Montserrat", Arial, sans-serif;
    font-weight: 700;
    font-size: 31px;
    color: var(--black);
    letter-spacing: -0.2px;
  }
  .features {
    position: absolute;
    left: 21px;
    top: 162px;
    list-style: none;
    font-weight: 700;
    font-size: 23px;
    line-height: 37px;
    color: var(--black);
  }
  .features li::before { content: "| "; }
  .slogan-lead {
    position: absolute;
    left: 0;
    width: 515px;
    top: 400px;
    text-align: center;
    font-weight: 700;
    font-size: 28px;
    color: var(--black);
  }
  .slogan-script {
    position: absolute;
    left: 0;
    width: 515px;
    top: 442px;
    text-align: center;
    font-family: "Kaushan Script", cursive;
    font-size: 46px;
    line-height: 62px;
    color: var(--black);
  }
  .brand-panel {
    position: absolute;
    left: 549px;
    top: 166px;
    width: 651px;
    height: 232px;
    background: var(--black);
    display: flex;
    align-items: center;
    justify-content: center;
    gap: 22px;
  }
  .brand-mark {
    width: 26px;
    height: 26px;
    background: var(--gold);
  }
  .brand-name {
    font-family: "Montserrat", Arial, sans-serif;
    font-weight: 500;
    font-size: 62px;
    color: var(--white);
    letter-spacing: 0.5px;
  }
  .contact-bar {
    position: absolute;
    left: 0;
    top: 597px;
    width: 1200px;
    height: 89px;
    background: var(--black);
    display: flex;
    align-items: center;
    justify-content: flex-end;
    padding-right: 32px;
    font-weight: 700;
    font-size: 28px;
    color: var(--white);
    white-space: nowrap;
  }
</style>
</head>
<body>
  <div class="card">
    <div class="honeycomb-area" role="img" aria-label="Gold honeycomb pattern of hexagons with thin white gaps"></div>

    <svg class="banner" viewBox="0 0 545 290" aria-hidden="true">
      <polygon points="0,17 476,17 545,146 476,290 0,290" fill="#0b0b0b"/>
      <polygon points="0,0 459,0 523,129 459,266 0,266" fill="#f9dc14"/>
    </svg>

    <h2 class="banner-title">Quality Dental Care</h2>
    <ul class="features">
      <li>15 Years of Service</li>
      <li>Quality Dental Treament</li>
      <li>Specialized Dentists</li>
      <li>Modern Technology</li>
    </ul>

    <p class="slogan-lead">Your Solution to a</p>
    <p class="slogan-script">Healthy, Beautiful<br>Smile</p>

    <div class="brand-panel">
      <span class="brand-mark"></span>
      <span class="brand-name">dr Corbescu</span>
    </div>

    <footer class="contact-bar">Address 123, Anywhere 12345 | 123.455.7867 | www.website.com</footer>
  </div>
</body>
</html>
```